Pivots & Treads .com

This website is simple!!!
Landing page background image should capture the customers attention!!! We will provide a image as a example of what we like. The purpose for this website is to provide customers with a clean easy way to request a quote for industrial casters and wheels by OEM’s as well as maintenance departments worldwide. Please see if you can follow our thought process below.
Customer comes to website, they are invited to Request a Quote by providing us with Manufacturer Name, Manufacturers Part # and quantity needed.
If this is not known the customer will complete will WP conversation format form answering about 10 questions
Or
Look up the part number in one of the 8 to 12 catalogs located in the Flippin Book format on our catalog page, or equal plug in .
When the client request a quote a account page will pop up request The following:
Clients first and last name
Email address
And optional questions
Company name and best contact number.
Once this is complete customer will hit SUBMIT.
The customers request will be in system. A email will be sent to Customer service notifying us the Quote Request has been made.
We will then build a quote for the customer with a good, better and best options. Customers Request a Quote submission may have more than one caster or wheel requested at a time, so website must allow this.
When the customer comes back into website there email address will come up as the account name and request a password be made for them. This will allow them to store quotes in their account for future needs. If quote is older than 30 day the system will trigger a button at the bottom of the quote for resubmit Request for updated quote.
Once customer reviews quote the quote can be Converted to order within the website.
Once Converted the system will send us a email and order will be processed.
We will need a Chat program that will text to CS the questions.
You will need to have high quality graphic design skills on your team.
We have found 2 plugins that would work nicely with our new website Flippin books to showcase our catalogs for customers to research and WPForms conversation forms to complete request for quote form.
Just Ideas:
Very very ghosted caster blueprint in white background but very very ghosted or the icon just idea
We have never had a font used we like
Grayscale every except for rubber on wheels and logo icon
Website should have hamburger menu on left
Website should hav responsive deign
Account head on right side
Has anyone read the brief from top to bottom and the updates, I’m seeing a lot of duplicates of the website I posted in images I want a clean website With lite backgrand with the poly being definite colors on each wheel I added a green yellow and red image has anyone looked at that Just a question?
Went on vacation/holiday

```html
<!DOCTYPE html>
<html lang="en">
<head>
<meta charset="utf-8">
<title>Pivots &amp; Treads — Landing Page Layouts</title>
<link href="https://fonts.googleapis.com/css2?family=Exo+2:wght@400;500;600;700&family=Montserrat:wght@700;800&family=Roboto:wght@400;500&display=swap" rel="stylesheet">
<style>
:root{
  --navy:#2c4399;
  --navy-deep:#233886;
  --band:#3a4f9f;
  --band-dark:#31448f;
  --accent:#4d69d9;
  --ice:#bccaf2;
  --ink:#2a2a2a;
  --muted:#555;
  --soft:#777;
  --hero-a:#f5f5f5;
  --hero-b:#e2e2e2;
  --board:#b4b4b4;
  --foot:#efefef;
  --white:#fff;
}
*{margin:0;padding:0;box-sizing:border-box}
html,body{width:848px;height:1200px;overflow:hidden}
body{background:var(--board);position:relative;font-family:"Exo 2",sans-serif;color:var(--ink)}
.page{position:absolute;top:30px;width:362px;background:var(--white);overflow:hidden}
.page--full{left:46px;height:1139px}
.page--short{left:441.5px;height:754px}
.abs{position:absolute}

/* hero */
.hero{position:absolute;left:0;top:0;width:362px;height:194px;z-index:2;
  background:linear-gradient(125deg,var(--hero-a) 0%,#ececec 35%,var(--hero-b) 60%,#efefef 100%)}
.brand-mark{position:absolute;left:33px;top:10px;display:flex;align-items:center;gap:3px;
  font-family:"Exo 2",sans-serif;font-weight:700;font-size:6.5px;color:var(--navy)}
.brand-mark__dot{width:7px;height:7px;border-radius:50%;background:var(--navy)}
.menu-icon{position:absolute;left:320px;top:10px;width:7px}
.menu-icon span{display:block;height:1.2px;background:#222;margin-bottom:1.3px}
.hero__title{position:absolute;left:33px;top:61px;font-family:"Montserrat",sans-serif;font-weight:800;
  font-size:13.2px;letter-spacing:.2px;color:var(--navy)}
.hero__tagline{position:absolute;left:33px;top:82px;font-family:"Roboto",sans-serif;font-weight:500;font-size:6.5px;color:#555}
.hero__easy{position:absolute;left:33px;top:94px;font-family:"Roboto",sans-serif;font-size:4.9px;color:#444}
.hero__steps{position:absolute;left:33px;top:105px;list-style:none;font-family:"Roboto",sans-serif;font-size:4.9px;color:#444}
.hero__steps li{display:flex;align-items:center;gap:4px;height:9px}
.hero__steps svg{width:5px;height:5px}
.btn-hero{position:absolute;top:140px;height:12.5px;background:var(--navy);color:#fff;
  font-family:"Roboto",sans-serif;font-weight:500;font-size:4.2px;letter-spacing:.1px;
  display:flex;align-items:center;justify-content:center;gap:3px}
.btn-hero--quote{left:33px;width:56px}
.btn-hero--catalog{left:93px;width:40px}
.btn-hero svg{width:3.5px;height:3.5px}
.hero__visual{position:absolute;left:185px;top:44px;width:150px;height:138px;border-radius:40% 40% 48% 48%;
  background:radial-gradient(ellipse at 55% 70%,#34477f 0%,#2b3a6e 38%,#8b93a8 62%,#cfd0d4 80%,rgba(226,226,226,0) 100%)}

/* about */
.about{position:absolute;left:0;top:194px;width:362px;height:196px;background:#fff}
.about__photo{position:absolute;left:33px;top:30px;width:134px;height:133px;background:#9a9a9a;border-radius:2px;padding:4px}
.about__photo-fill{width:100%;height:100%;border:2.5px solid #fff;
  background:linear-gradient(180deg,#5d6166 0%,#8c9095 40%,#b7babd 75%,#a4a7aa 100%)}
.about__title{position:absolute;left:185px;top:30px;font-weight:600;font-size:9px;color:#1d1d1d}
.rule{position:absolute;height:1px;width:20px;background:var(--navy)}
.about__text{position:absolute;left:185px;width:143px;font-size:5px;line-height:7.8px;text-align:justify;color:#333}
.pill{position:absolute;border-radius:8px;display:flex;align-items:center;justify-content:center;font-weight:500;font-size:5.6px}
.pill--blue{background:var(--navy);color:#fff;box-shadow:0 1px 2px rgba(0,0,0,.3)}
.pill--white{background:#fff;color:var(--navy)}

/* products */
.products{position:absolute;left:0;width:362px}
.products--band{top:390px;height:410px;background:linear-gradient(160deg,#4658a5 0%,var(--band) 45%,#34478f 100%)}
.products--plain{top:189px;height:376px;background:#fff}
.products__title{position:absolute;left:0;width:100%;top:30px;text-align:center;font-weight:600;font-size:9px}
.products--band .products__title{color:#fff}
.products--plain .products__title{color:#111}
.products__intro{position:absolute;left:0;width:100%;top:53px;text-align:center;font-size:5.3px;line-height:7.8px}
.products--band .products__intro{color:#fff}
.products--plain .products__intro{color:#333}
.catalog{position:absolute;left:0;top:83px;width:362px;height:300px}
.catalog__bar{position:absolute;left:0;top:0;width:362px;height:24px;border-top:1px solid rgba(255,255,255,.5);border-bottom:1px solid rgba(255,255,255,.5)}
.products--plain .catalog__bar{border-color:var(--navy)}
.catalog__label{position:absolute;left:0;top:0;width:72px;height:24px;display:flex;align-items:center;justify-content:center;
  font-weight:700;font-size:9.5px;color:#fff;background:rgba(40,58,130,.45)}
.products--plain .catalog__label{background:var(--band);top:-1px;height:24px}
.catalog__search{position:absolute;left:79px;top:0;height:22px;display:flex;align-items:center;font-size:6px}
.products--band .catalog__search{color:rgba(255,255,255,.75)}
.products--plain .catalog__search{color:#666}
.filters{position:absolute;left:0;top:24px;width:72px;height:238px}
.products--band .filters{background:rgba(38,55,128,.35);border-right:1px solid rgba(255,255,255,.45);border-bottom:1px solid rgba(255,255,255,.45)}
.products--plain .filters{background:var(--band)}
.filters__group{list-style:none;padding-left:16px;color:#fff}
.filters__group + .filters__group{border-top:1px solid rgba(255,255,255,.45)}
.filters__group--type{height:64px;padding-top:6px}
.filters__group--materials{height:104px;padding-top:9px}
.filters__group--second{height:70px;padding-top:12px}
.filters__heading{font-size:5.8px;height:11px;line-height:11px}
.filters__item{font-size:5px;height:12.7px;line-height:12.7px;display:flex;align-items:center;gap:3px}
.filters__item::before{content:"";width:3.6px;height:3.6px;border:0.6px solid #fff}
.product-grid{position:absolute;left:80px;top:32px;display:grid;grid-template-columns:repeat(4,60px);grid-auto-rows:69px;column-gap:6.7px;row-gap:9px}
.product-card{background:#fff;display:flex;align-items:center;justify-content:center}
.products--band .product-card{padding:2.5px}
.products--band .product-card__inner{border:0.6px solid #8a8a8a}
.products--plain .product-card{border:2.5px solid var(--ice)}
.product-card__inner{width:100%;height:100%;display:flex;align-items:center;justify-content:center;background:#fff}
.product-card__photo{width:44px;height:44px;border-radius:50%;
  background:radial-gradient(circle at 50% 50%,#d4d4d4 0%,#9a9a9a 18%,#2f2f2f 40%,#1c1c1c 70%,#5b5b5b 100%)}
.product-card__photo--blue{background:radial-gradient(circle at 55% 60%,#b5b5b5 0%,#7c7c7c 15%,#2f3f7a 35%,#1f2b57 70%,#8f96aa 100%);border-radius:45% 45% 50% 50%}
.product-card__photo--silver{background:radial-gradient(circle at 50% 50%,#eee 0%,#9c9c9c 30%,#5a5a5a 55%,#b5b5b5 80%,#777 100%)}
.product-card--feature{background:var(--accent)}
.products--band .product-card--feature{padding:2.5px;background:#fff}
.product-card--feature .product-card__inner{background:var(--accent);flex-direction:column;color:#fff;text-align:center;border:none}
.products--plain .product-card--feature{border-color:#9db0ea;box-shadow:0 1px 2px rgba(0,0,0,.3)}
.feature__title{font-weight:600;font-size:5.5px;margin-bottom:3px}
.feature__text{font-size:3.9px;line-height:6.1px;padding:0 5px}
.feature__link{font-weight:700;font-size:4.6px;text-decoration:underline;margin-top:3px}
.catalog__more{left:162px;top:283px;width:40px;height:15px}

/* how it works */
.steps{position:absolute;left:0;top:800px;width:362px;height:160px;background:#fff}
.steps__title{position:absolute;left:0;width:100%;top:28px;text-align:center;font-weight:600;font-size:9px;color:#111}
.steps__links{position:absolute;left:0;top:0}
.step{position:absolute;top:58px;width:100px;text-align:center}
.step__icon{width:46px;height:46px;border-radius:50%;background:#fff;margin:0 auto;box-shadow:0 1px 3px rgba(0,0,0,.25);display:flex;align-items:center;justify-content:center}
.step__icon svg{width:22px;height:22px}
.step__name{margin-top:10px;font-weight:700;font-size:6.4px;color:var(--navy)}
.step__text{margin-top:2px;font-size:5px;line-height:7.8px;color:#555}

/* footer */
.footer{position:absolute;left:0;width:362px;height:189px}
.page--full .footer{top:950px}
.page--short .footer{top:565px}
.footer__wave{position:absolute;left:0;top:0}
.chat-button{position:absolute;left:16px;top:3px;width:34px;height:34px;border-radius:50%;background:var(--navy);
  border:2px solid #fff;box-shadow:0 2px 4px rgba(0,0,0,.35);display:flex;align-items:center;justify-content:center}
.chat-button svg{width:14px;height:14px}
.footer__col{position:absolute;top:70px}
.footer__heading{font-weight:600;font-size:6.2px;color:#111;height:9px}
.footer__heading::after{content:"";display:block;margin-top:2px;width:40px;height:1.2px;background:linear-gradient(90deg,#111 60%,rgba(17,17,17,0))}
.footer__links{list-style:none;margin-top:8px}
.footer__links li{font-size:4.8px;height:11.4px;color:#333}
.footer__links li::before{content:"» ";font-weight:700}
.contact{list-style:none;margin-top:8px;width:62px}
.contact li{display:flex;gap:3px;font-size:4.6px;line-height:6px;color:#333;padding-bottom:3px;margin-bottom:4px;border-bottom:0.6px solid #888}
.contact svg{width:5px;height:5px;flex:none;margin-top:.5px}
.footer__brand{position:absolute;left:244px;top:67px;width:85px}
.footer__brand-name{display:flex;align-items:center;gap:3px;font-weight:700;font-size:6px;color:#111}
.footer__brand-name span.square{width:9px;height:9px;background:#111}
.footer__about{margin-top:14px;font-size:4.6px;line-height:6px;text-align:justify;color:#333}
.socials{display:flex;gap:9px;margin-top:7px}
.socials span{width:9.5px;height:9.5px;border-radius:50%;border:0.7px solid #111}
.footer__rule{position:absolute;left:33px;top:158px;width:295px;height:0.6px;background:#555}
.footer__copy{position:absolute;left:0;width:100%;top:170px;text-align:center;font-size:4.4px;color:#222}
</style>
</head>
<body>

<!-- ========== Full landing page ========== -->
<section class="page page--full">
  <header class="hero">
    <div class="brand-mark"><span class="brand-mark__dot"></span>Pivots &amp; Treads</div>
    <div class="menu-icon"><span></span><span></span><span></span></div>
    <h1 class="hero__title">PIVOTS &amp; TREADS</h1>
    <p class="hero__tagline"># 1 Solutions for all your Applications</p>
    <p class="hero__easy">Easy as 1 - 2 - 3</p>
    <ul class="hero__steps">
      <li><svg viewBox="0 0 10 10"><circle cx="5" cy="5" r="4.2" fill="none" stroke="#2c4399" stroke-width="1.4"/><path d="M3 5.2l1.5 1.5 2.6-3" fill="none" stroke="#2c4399" stroke-width="1.3"/></svg>Request a Quote</li>
      <li><svg viewBox="0 0 10 10"><circle cx="5" cy="5" r="4.2" fill="none" stroke="#2c4399" stroke-width="1.4"/><path d="M3 5.2l1.5 1.5 2.6-3" fill="none" stroke="#2c4399" stroke-width="1.3"/></svg>Receive a Quote</li>
      <li><svg viewBox="0 0 10 10"><circle cx="5" cy="5" r="4.2" fill="none" stroke="#2c4399" stroke-width="1.4"/><path d="M3 5.2l1.5 1.5 2.6-3" fill="none" stroke="#2c4399" stroke-width="1.3"/></svg>Convert a Quote to order</li>
    </ul>
    <a class="btn-hero btn-hero--quote">REQUEST A QUOTE <svg viewBox="0 0 10 10"><circle cx="5" cy="5" r="5" fill="#fff"/><path d="M4 2.8l2.2 2.2L4 7.2" fill="none" stroke="#2c4399" stroke-width="1.5"/></svg></a>
    <a class="btn-hero btn-hero--catalog">CATALOG <svg viewBox="0 0 10 10"><circle cx="5" cy="5" r="5" fill="#fff"/><path d="M4 2.8l2.2 2.2L4 7.2" fill="none" stroke="#2c4399" stroke-width="1.5"/></svg></a>
    <div class="hero__visual" role="img" aria-label="Swivel caster with a silver plate and navy wheel"></div>
  </header>

  <section class="about">
    <div class="about__photo"><div class="about__photo-fill" role="img" aria-label="Empty industrial warehouse interior"></div></div>
    <h2 class="about__title">About Pivots &amp; Treads</h2>
    <span class="rule" style="left:185px;top:45px"></span>
    <p class="about__text" style="top:53px">Ut enim ad minim veniam, quis nostrud exercitation ullamco laboris nisi ut aliquip ex ea commodo consequat. Duis aute irure dolor in reprehenderit in voluptate eiusmod tempor incididunt ut labore e velit esse cillum dolore eu fugiat nulla pariatur. Excepteur sint occaecat cupidatat non proident, sunt in culpa qui officia deserunt mollit anim id est laborum.</p>
    <p class="about__text" style="top:122px">Ut enim ad minima veniam, quis nostrum exercitationem ullam corporis suscipit commodi consequatur.</p>
    <a class="pill pill--blue" style="left:185px;top:145px;width:46px;height:15px">Read More</a>
  </section>

  <section class="products products--band">
    <h2 class="products__title">Our Product</h2>
    <p class="products__intro">Duis aute irure dolor in reprehenderit in voluptate Quis autem vel eum iure<br>reprehenderit velit esse cillum dolore eu fugiat nulla pariatur.</p>
    <div class="catalog">
      <div class="catalog__bar"></div>
      <div class="catalog__label">Catalog</div>
      <div class="catalog__search">Search Product......</div>
      <aside class="filters">
        <ul class="filters__group filters__group--type">
          <li class="filters__heading">TYPE</li>
          <li class="filters__item">All Types</li><li class="filters__item">Velit Esse</li><li class="filters__item">Dolore</li>
        </ul>
        <ul class="filters__group filters__group--materials">
          <li class="filters__heading">MATERIALS</li>
          <li class="filters__item">Consectetur</li><li class="filters__item">Undeomnis</li><li class="filters__item">Perspiciatis</li><li class="filters__item">Voluptas</li><li class="filters__item">Explicabo</li><li class="filters__item">Numquam</li>
        </ul>
        <ul class="filters__group filters__group--second">
          <li class="filters__heading">TYPE</li>
          <li class="filters__item">All Types</li><li class="filters__item">Velit Esse</li><li class="filters__item">Dolore</li>
        </ul>
      </aside>
      <div class="product-grid">
        <div class="product-card"><div class="product-card__inner"><div class="product-card__photo product-card__photo--blue" role="img" aria-label="Swivel caster with navy wheel"></div></div></div>
        <div class="product-card product-card--feature"><div class="product-card__inner"><p class="feature__title">Finibus Bonorum</p><p class="feature__text">Ut enim ad minim veniam, quis nostrud exercitation ullamco laboris nisi ut aliquip ex ea commodo.</p><p class="feature__link">SHOP NOW</p></div></div>
        <div class="product-card"><div class="product-card__inner"><div class="product-card__photo" role="img" aria-label="Black cast iron V-groove wheel"></div></div></div>
        <div class="product-card"><div class="product-card__inner"><div class="product-card__photo product-card__photo--silver" role="img" aria-label="Grey spoked pulley wheel"></div></div></div>
        <div class="product-card"><div class="product-card__inner"><div class="product-card__photo" role="img" aria-label="Rigid caster with black wheel"></div></div></div>
        <div class="product-card"><div class="product-card__inner"><div class="product-card__photo" role="img" aria-label="Black idler pulley"></div></div></div>
        <div class="product-card"><div class="product-card__inner"><div class="product-card__photo product-card__photo--silver" role="img" aria-label="Silver alloy wheel rim"></div></div></div>
        <div class="product-card"><div class="product-card__inner"><div class="product-card__photo" role="img" aria-label="Black flat idler pulley"></div></div></div>
        <div class="product-card"><div class="product-card__inner"><div class="product-card__photo product-card__photo--silver" role="img" aria-label="Black tyre with silver hub"></div></div></div>
        <div class="product-card"><div class="product-card__inner"><div class="product-card__photo product-card__photo--blue" role="img" aria-label="Braked swivel caster with blue wheel"></div></div></div>
        <div class="product-card"><div class="product-card__inner"><div class="product-card__photo" role="img" aria-label="Black pulley with bolt holes"></div></div></div>
        <div class="product-card"><div class="product-card__inner"><div class="product-card__photo product-card__photo--silver" role="img" aria-label="Grey multi-groove pulley"></div></div></div>
      </div>
      <a class="pill pill--white abs catalog__more">View All</a>
    </div>
  </section>

  <section class="steps">
    <h2 class="steps__title">How Its Work</h2>
    <span class="rule" style="left:171px;top:45px"></span>
    <svg class="steps__links" width="362" height="160" viewBox="0 0 362 160">
      <path d="M103 80 C125 70 145 70 160 76" fill="none" stroke="#2c4399" stroke-width="0.6" stroke-dasharray="1.5 1.5"/>
      <path d="M209 76 C228 88 250 88 265 80" fill="none" stroke="#2c4399" stroke-width="0.6" stroke-dasharray="1.5 1.5"/>
    </svg>
    <div class="step" style="left:29px">
      <div class="step__icon"><svg viewBox="0 0 24 24" fill="none" stroke="#2c4399" stroke-width="1"><rect x="3" y="5" width="15" height="11" rx="1"/><path d="M8 19h6M11 16v3"/><circle cx="17" cy="7" r="4" fill="#fff"/><path d="M17 6v3M17 4.7v.3"/></svg></div>
      <p class="step__name">Request A quote</p>
      <p class="step__text">Excepteur sint occaecat cupidatat non proident, sunt in culpa qui officia deserunt id est laborum.</p>
    </div>
    <div class="step" style="left:135px">
      <div class="step__icon"><svg viewBox="0 0 24 24" fill="none" stroke="#2c4399" stroke-width="1"><rect x="6" y="3" width="12" height="17" rx="1"/><path d="M8.5 7h7M8.5 10h7M8.5 13h3M13 13h2.5M8.5 16h7"/></svg></div>
      <p class="step__name">Recive A quote</p>
      <p class="step__text">Duis aute irure dolor in repreheerit in voluptate velit esse cillum dolore eu fugiat nulla pariatur.</p>
    </div>
    <div class="step" style="left:239px">
      <div class="step__icon"><svg viewBox="0 0 24 24" fill="none" stroke="#2c4399" stroke-width="1"><path d="M5 12a7 7 0 0 1 12-5M19 12a7 7 0 0 1-12 5"/><path d="M17 3.5V7h-3.5M7 20.5V17h3.5"/><path d="M10 9l5 3-5 3z"/></svg></div>
      <p class="step__name">Convert a quote to order</p>
      <p class="step__text">Quis autem vel eum iure reprehenderit qui in ea voluptate velit esse quam nihil molestiae</p>
    </div>
  </section>

  <footer class="footer">
    <svg class="footer__wave" width="362" height="189" viewBox="0 0 362 189">
      <path d="M0 14 C110 40 260 36 362 10 L362 189 L0 189 Z" fill="#efefef"/>
      <path d="M0 14 C110 40 260 36 362 10" fill="none" stroke="#2c4399" stroke-width="2"/>
    </svg>
    <div class="chat-button"><svg viewBox="0 0 24 24" fill="none" stroke="#fff" stroke-width="1.4"><path d="M3 4h13v9H8l-3 3v-3H3z"/><path d="M16 8h5v9h-2v3l-3-3h-6v-4"/><path d="M6 7.5h7M6 10h5"/></svg></div>
    <div class="footer__col" style="left:33px">
      <p class="footer__heading">QUICK LINKS</p>
      <ul class="footer__links"><li>Home</li><li>About</li><li>Product</li><li>Why choose us</li><li>Blog</li></ul>
    </div>
    <div class="footer__col" style="left:97px">
      <p class="footer__heading">HELP CENTER</p>
      <ul class="footer__links"><li>FAQ</li><li>Privacy</li><li>Condition</li><li>Terms</li><li>Contact</li></ul>
    </div>
    <div class="footer__col" style="left:158px">
      <p class="footer__heading">CONTACT US</p>
      <ul class="contact">
        <li><svg viewBox="0 0 10 10" fill="none" stroke="#333" stroke-width=".8"><path d="M5 9.5S1.8 6 1.8 4a3.2 3.2 0 0 1 6.4 0C8.2 6 5 9.5 5 9.5z"/><circle cx="5" cy="4" r="1.2"/></svg><span>Pivots &amp; Treads<br>Harbor Row<br>Oakridge</span></li>
        <li><svg viewBox="0 0 10 10" fill="none" stroke="#333" stroke-width=".8"><rect x="1" y="2.5" width="8" height="5.5"/><path d="M1 2.5l4 3 4-3"/></svg><span>hello@pivotstreads.example</span></li>
        <li><svg viewBox="0 0 10 10" fill="none" stroke="#333" stroke-width=".8"><path d="M2 1.5h2l1 2-1.2 1a5 5 0 0 0 2.7 2.7l1-1.2 2 1v2A7 7 0 0 1 2 1.5z"/></svg><span>+1 555 014 7720</span></li>
      </ul>
    </div>
    <div class="footer__brand">
      <p class="footer__brand-name"><span class="square"></span>PIVOTS &amp; TREADS .com</p>
      <p class="footer__about">Excepteur sint occaecat cupidatat non proident, sunt in culpa qui officia deserunt mollit anim id est cillum dolore eu fugiat nulla pariatur laborum.</p>
      <div class="socials"><span></span><span></span><span></span><span></span></div>
    </div>
    <div class="footer__rule"></div>
    <p class="footer__copy">Copyrights@2022.All Rights Reserved</p>
  </footer>
</section>

<!-- ========== Short landing page ========== -->
<section class="page page--short">
  <header class="hero">
    <div class="brand-mark"><span class="brand-mark__dot"></span>Pivots &amp; Treads</div>
    <div class="menu-icon"><span></span><span></span><span></span></div>
    <h1 class="hero__title">PIVOTS &amp; TREADS</h1>
    <p class="hero__tagline"># 1 Solutions for all your Applications</p>
    <p class="hero__easy">Easy as 1 - 2 - 3</p>
    <ul class="hero__steps">
      <li><svg viewBox="0 0 10 10"><circle cx="5" cy="5" r="4.2" fill="none" stroke="#2c4399" stroke-width="1.4"/><path d="M3 5.2l1.5 1.5 2.6-3" fill="none" stroke="#2c4399" stroke-width="1.3"/></svg>Request a Quote</li>
      <li><svg viewBox="0 0 10 10"><circle cx="5" cy="5" r="4.2" fill="none" stroke="#2c4399" stroke-width="1.4"/><path d="M3 5.2l1.5 1.5 2.6-3" fill="none" stroke="#2c4399" stroke-width="1.3"/></svg>Receive a Quote</li>
      <li><svg viewBox="0 0 10 10"><circle cx="5" cy="5" r="4.2" fill="none" stroke="#2c4399" stroke-width="1.4"/><path d="M3 5.2l1.5 1.5 2.6-3" fill="none" stroke="#2c4399" stroke-width="1.3"/></svg>Convert a Quote to order</li>
    </ul>
    <a class="btn-hero btn-hero--quote">REQUEST A QUOTE <svg viewBox="0 0 10 10"><circle cx="5" cy="5" r="5" fill="#fff"/><path d="M4 2.8l2.2 2.2L4 7.2" fill="none" stroke="#2c4399" stroke-width="1.5"/></svg></a>
    <a class="btn-hero btn-hero--catalog">CATALOG <svg viewBox="0 0 10 10"><circle cx="5" cy="5" r="5" fill="#fff"/><path d="M4 2.8l2.2 2.2L4 7.2" fill="none" stroke="#2c4399" stroke-width="1.5"/></svg></a>
    <div class="hero__visual" role="img" aria-label="Swivel caster with a silver plate and navy wheel"></div>
  </header>

  <section class="products products--plain">
    <h2 class="products__title">Our Product</h2>
    <span class="rule" style="left:171px;top:47px;background:#111"></span>
    <p class="products__intro">Duis aute irure dolor in reprehenderit in voluptate Quis autem vel eum iure<br>reprehenderit velit esse cillum dolore eu fugiat nulla pariatur.</p>
    <div class="catalog">
      <div class="catalog__bar"></div>
      <div class="catalog__label">Catalog</div>
      <div class="catalog__search">Search Product......</div>
      <aside class="filters">
        <ul class="filters__group filters__group--type">
          <li class="filters__heading">TYPE</li>
          <li class="filters__item">All Types</li><li class="filters__item">Velit Esse</li><li class="filters__item">Dolore</li>
        </ul>
        <ul class="filters__group filters__group--materials">
          <li class="filters__heading">MATERIALS</li>
          <li class="filters__item">Consectetur</li><li class="filters__item">Undeomnis</li><li class="filters__item">Perspiciatis</li><li class="filters__item">Voluptas</li><li class="filters__item">Explicabo</li><li class="filters__item">Numquam</li>
        </ul>
        <ul class="filters__group filters__group--second">
          <li class="filters__heading">TYPE</li>
          <li class="filters__item">All Types</li><li class="filters__item">Velit Esse</li><li class="filters__item">Dolore</li>
        </ul>
      </aside>
      <div class="product-grid">
        <div class="product-card"><div class="product-card__inner"><div class="product-card__photo product-card__photo--blue" role="img" aria-label="Swivel caster with navy wheel"></div></div></div>
        <div class="product-card product-card--feature"><div class="product-card__inner"><p class="feature__title">Finibus Bonorum</p><p class="feature__text">Ut enim ad minim veniam, quis nostrud exercitation ullamco laboris nisi ut aliquip ex ea commodo.</p><p class="feature__link">SHOP NOW</p></div></div>
        <div class="product-card"><div class="product-card__inner"><div class="product-card__photo" role="img" aria-label="Black cast iron V-groove wheel"></div></div></div>
        <div class="product-card"><div class="product-card__inner"><div class="product-card__photo product-card__photo--silver" role="img" aria-label="Grey spoked pulley wheel"></div></div></div>
        <div class="product-card"><div class="product-card__inner"><div class="product-card__photo" role="img" aria-label="Rigid caster with black wheel"></div></div></div>
        <div class="product-card"><div class="product-card__inner"><div class="product-card__photo" role="img" aria-label="Black idler pulley"></div></div></div>
        <div class="product-card"><div class="product-card__inner"><div class="product-card__photo product-card__photo--silver" role="img" aria-label="Silver alloy wheel rim"></div></div></div>
        <div class="product-card"><div class="product-card__inner"><div class="product-card__photo" role="img" aria-label="Black flat idler pulley"></div></div></div>
        <div class="product-card"><div class="product-card__inner"><div class="product-card__photo product-card__photo--silver" role="img" aria-label="Black tyre with silver hub"></div></div></div>
        <div class="product-card"><div class="product-card__inner"><div class="product-card__photo product-card__photo--blue" role="img" aria-label="Braked swivel caster with blue wheel"></div></div></div>
        <div class="product-card"><div class="product-card__inner"><div class="product-card__photo" role="img" aria-label="Black pulley with bolt holes"></div></div></div>
        <div class="product-card"><div class="product-card__inner"><div class="product-card__photo product-card__photo--silver" role="img" aria-label="Grey multi-groove pulley"></div></div></div>
      </div>
      <a class="pill pill--blue abs catalog__more">View All</a>
    </div>
  </section>

  <footer class="footer">
    <svg class="footer__wave" width="362" height="189" viewBox="0 0 362 189">
      <path d="M0 14 C110 40 260 36 362 10 L362 189 L0 189 Z" fill="#efefef"/>
      <path d="M0 14 C110 40 260 36 362 10" fill="none" stroke="#2c4399" stroke-width="2"/>
    </svg>
    <div class="chat-button"><svg viewBox="0 0 24 24" fill="none" stroke="#fff" stroke-width="1.4"><path d="M3 4h13v9H8l-3 3v-3H3z"/><path d="M16 8h5v9h-2v3l-3-3h-6v-4"/><path d="M6 7.5h7M6 10h5"/></svg></div>
    <div class="footer__col" style="left:33px">
      <p class="footer__heading">QUICK LINKS</p>
      <ul class="footer__links"><li>Home</li><li>About</li><li>Product</li><li>Why choose us</li><li>Blog</li></ul>
    </div>
    <div class="footer__col" style="left:94px">
      <p class="footer__heading">HELP CENTER</p>
      <ul class="footer__links"><li>FAQ</li><li>Privacy</li><li>Condition</li><li>Terms</li><li>Contact</li></ul>
    </div>
    <div class="footer__col" style="left:156px">
      <p class="footer__heading">CONTACT US</p>
      <ul class="contact">
        <li><svg viewBox="0 0 10 10" fill="none" stroke="#333" stroke-width=".8"><path d="M5 9.5S1.8 6 1.8 4a3.2 3.2 0 0 1 6.4 0C8.2 6 5 9.5 5 9.5z"/><circle cx="5" cy="4" r="1.2"/></svg><span>Pivots &amp; Treads<br>Harbor Row<br>Oakridge</span></li>
        <li><svg viewBox="0 0 10 10" fill="none" stroke="#333" stroke-width=".8"><rect x="1" y="2.5" width="8" height="5.5"/><path d="M1 2.5l4 3 4-3"/></svg><span>hello@pivotstreads.example</span></li>
        <li><svg viewBox="0 0 10 10" fill="none" stroke="#333" stroke-width=".8"><path d="M2 1.5h2l1 2-1.2 1a5 5 0 0 0 2.7 2.7l1-1.2 2 1v2A7 7 0 0 1 2 1.5z"/></svg><span>+1 555 014 7720</span></li>
      </ul>
    </div>
    <div class="footer__brand" style="left:241px">
      <p class="footer__brand-name"><span class="square"></span>PIVOTS &amp; TREADS .com</p>
      <p class="footer__about">Excepteur sint occaecat cupidatat non proident, sunt in culpa qui officia deserunt mollit anim id est cillum dolore eu fugiat nulla pariatur laborum.</p>
      <div class="socials"><span></span><span></span><span></span><span></span></div>
    </div>
    <div class="footer__rule" style="left:30px"></div>
    <p class="footer__copy">Copyrights@2022.All Rights Reserved</p>
  </footer>
</section>

</body>
</html>
```